Curtain Cleaning Flyer to be designed for Singapore market

We are a laundry company providing curtain cleaning services to Singapore market. We have a company vehicle pickup and provide dismantling of curtain at customer house. The dismantled curtain will be weighed and quote will be given to customer immediately. If they accept the price, we will delivered and installed the clean curtain to them.
Refer to our website for more information https://www.glimmerloft.com.sg/curtain-cleaning
The flyer will be distributed to higher income level people in Singapore staying in condominium/semi detached or bungalow.
I need a well designed flyers to engage people to use my service. So please help.

Target Market(s)

Singapore market

Industry/Entity Type

It Company

Requirements
Must have
• MUST INCLUDE CURTAINS pictures in design to let people know it is for curtain laundry
• 1) Flyer has to be eye catching and engage people to call and use our curtain cleaning services.
• 2) It has to professional.
• 3) It has to provide clear information of the following (see curtain cleaning picture I have provided)
• Curtain Laundry at $10/kg
• Call 8614 2253
• No Hidden Cost
• Include Pickup, Dismantle, Installation and Delivery
• 4) Provide company information:
• GLIMMER LOFT, Reg No.71840362K
• 47 Kelvin Brook Road
• Singapore 073194
• https://www.glimmerloft.com.sg/curtain-cleaning
• Email: enquiries@glimmerloft.com.sg
• Tel: +65 8614 2253
• 5) Include our company logo but do not use it extensively.
Nice to have
• Nice to have a compelling action design for people to call and use my service.
• Nice to highlight on the good laundry price $10 per kg for curtain laundry
• Nice to be professional and cute
Should not have
• Complicated
• No design on woman wearing low cut dresses for promotion

```html
<!DOCTYPE html>
<html lang="en">
<head>
<meta charset="utf-8">
<title>Glimmer Loft – Curtain Laundry Flyer</title>
<link rel="stylesheet" href="https://fonts.googleapis.com/css2?family=Open+Sans:wght@400;600;700&family=Arvo:wght@700&family=Roboto:wght@700&display=swap">
<style>
  :root {
    --stage: #d4d5d7;
    --paper: #ffffff;
    --navy: #0a64ad;
    --blue: #1a73ba;
    --teal: #2fb0a6;
    --green: #1d9a6e;
    --mint: #e2f4f0;
    --sky: #4aa8df;
    --footer-text: #6fd0c9;
    --ink: #111111;
  }
  * { margin: 0; padding: 0; box-sizing: border-box; }
  html, body { width: 890px; height: 1200px; overflow: hidden; }
  body { background: var(--stage); font-family: "Open Sans", sans-serif; position: relative; }

  .flyer {
    position: absolute; left: 59px; top: 54px;
    width: 772px; height: 1133px;
    background: var(--paper);
    overflow: hidden;
  }

  .brand-mark {
    position: absolute; top: 118px; left: 0; width: 100%;
    display: flex; justify-content: center; align-items: center; gap: 16px;
  }
  .brand-mark__dot { width: 44px; height: 44px; border-radius: 50%; background: var(--sky); }
  .brand-mark__name { font-weight: 700; font-size: 50px; color: var(--sky); letter-spacing: 1px; }

  .banner {
    position: absolute; top: 239px; left: 0; width: 772px; height: 259px;
    background: var(--mint);
    border-top: 5px solid var(--navy);
  }
  .banner__photo {
    position: absolute; left: 0; top: 0; width: 360px; height: 100%;
    background: linear-gradient(90deg, #6f9aa0 0%, #8fb6b8 45%, #b8d8d4 75%, rgba(226,244,240,0) 100%);
  }
  .banner__offer {
    position: absolute; left: 352px; width: 400px; top: 0;
    text-align: center; font-family: "Arvo", serif; font-weight: 700; color: var(--green);
  }
  .banner__title { position: absolute; left: 0; width: 100%; top: 36px; font-size: 32px; line-height: 1; }
  .banner__price { position: absolute; left: 0; width: 100%; top: 90px; font-size: 32px; line-height: 1; }
  .banner__call  { position: absolute; left: 0; width: 100%; top: 140px; font-size: 26px; line-height: 1; }
  .banner__notes {
    position: absolute; left: 478px; top: 182px; z-index: 2;
    font-family: "Arvo", serif; font-weight: 700; font-size: 13px; line-height: 18px; color: var(--green);
  }
  .banner__wave { position: absolute; left: 0; bottom: 0; width: 772px; height: 110px; z-index: 1; }

  .headline {
    position: absolute; top: 560px; left: 0; width: 100%; text-align: center;
    font-weight: 600; font-size: 58px; color: var(--blue); line-height: 1;
  }
  .price {
    position: absolute; top: 646px; left: 0; width: 100%; text-align: center;
    font-weight: 600; font-size: 48px; color: var(--teal); line-height: 1;
  }
  .details {
    position: absolute; top: 750px; left: 0; width: 100%; text-align: center;
    font-size: 21px; line-height: 38px; color: var(--ink);
  }
  .company {
    position: absolute; top: 866px; left: 0; width: 100%; text-align: center;
    font-weight: 600; font-size: 50px; color: var(--teal); letter-spacing: 1px; line-height: 1;
  }
  .company-reg {
    position: absolute; top: 924px; left: 0; width: 100%; text-align: center;
    font-size: 20px; color: var(--ink);
  }

  .contact-bar {
    position: absolute; left: 0; bottom: 0; width: 100%; height: 154px;
    background: var(--navy); text-align: center;
  }
  .contact-bar__phone {
    position: absolute; top: 18px; left: 0; width: 100%;
    display: flex; justify-content: center; align-items: center; gap: 12px;
    font-family: "Roboto", sans-serif; font-weight: 700; font-size: 41px; color: #fff;
  }
  .contact-bar__phone svg { width: 32px; height: 32px; }
  .contact-bar__address { position: absolute; top: 76px; left: 0; width: 100%; font-size: 20px; color: var(--footer-text); }
  .contact-bar__links {
    position: absolute; top: 112px; left: 0; width: 100%;
    display: flex; justify-content: center; gap: 36px; font-size: 16px; color: var(--footer-text);
  }
</style>
</head>
<body>
  <main class="flyer">
    <div class="brand-mark">
      <span class="brand-mark__dot"></span>
      <span class="brand-mark__name">GLIMMER LOFT</span>
    </div>

    <section class="banner">
      <div class="banner__photo" role="img" aria-label="Photo of front-loading commercial washing machines in a laundry"></div>
      <div class="banner__offer">
        <div class="banner__title">Curtain Laundry</div>
        <div class="banner__price">$10/kg</div>
        <div class="banner__call">Call 8614 2253</div>
      </div>
      <div class="banner__notes">No Hidden Cost<br>Dismantle, Installation &amp; Delivery</div>
      <svg class="banner__wave" viewBox="0 0 772 110" preserveAspectRatio="none">
        <path d="M0 34 C200 62 350 108 520 104 C640 101 720 88 772 80 L772 110 L0 110 Z" fill="#1a8fd0"/>
        <path d="M0 46 C200 74 350 116 520 110 C640 106 720 94 772 88 L772 110 L0 110 Z" fill="#ffffff"/>
        <path d="M0 56 C200 84 350 122 520 116 C640 112 720 100 772 94 L772 110 L0 110 Z" fill="#1f7fc4"/>
        <path d="M0 70 C200 96 350 130 520 124 C640 120 720 106 772 102 L772 110 L0 110 Z" fill="#ffffff"/>
      </svg>
    </section>

    <h1 class="headline">CURTAIN LAUNDRY</h1>
    <p class="price">AT $10/kg</p>
    <p class="details">No Hidden Cost<br>Include Pickup, Dismantle, Installation and Delivery</p>

    <p class="company">GLIMMER LOFT</p>
    <p class="company-reg">Reg No.71840362K</p>

    <footer class="contact-bar">
      <div class="contact-bar__phone">
        <svg viewBox="0 0 24 24" aria-hidden="true"><path fill="#fff" d="M6.6 10.8a15.1 15.1 0 0 0 6.6 6.6l2.2-2.2c.3-.3.7-.4 1-.2 1.1.4 2.3.6 3.6.6.6 0 1 .4 1 1V20c0 .6-.4 1-1 1A17 17 0 0 1 3 4c0-.6.4-1 1-1h3.5c.6 0 1 .4 1 1 0 1.3.2 2.5.6 3.6.1.3 0 .7-.2 1z"/></svg>
        <span>+65 8614 2253</span>
      </div>
      <p class="contact-bar__address">47 Kelvin Brook Road Singapore 073194</p>
      <div class="contact-bar__links">
        <span>https://www.glimmerloft.com.sg/curtain-cleaning</span>
        <span>Email: enquiries@glimmerloft.com.sg</span>
      </div>
    </footer>
  </main>
</body>
</html>
```